Give us a remarkable appearance

We need a unique, remarkable stationery design (Business Cards, Business Letters, Email Signature etc.). The design should use our logo.

Verlan-Consulting is a startup in consulting, management and IT services and individual software development for the financial industry.

Verlan in english is agate stone. We would like to see designs that use colors out of the agate stone color range.

Preferred COLORS: gold, dark red (burgundy), white, dark grey, black ** see attached Logos **

The used font should be available for further usage with texts etc.

The design should express: modernity, precious, high quality, lightness, stability, ecological awareness, speedy, reliability, simplicity, sustainability.

Target Market(s)

C-Level and Business Clients, Professionals

Industry/Entity Type

Business

Logo Text

Logo styles of interest
Pictorial/Combination Logo
Abstract Logo
Wordmark Logo
Requirements
Must have
• Business Cards, Business Papers, Email Signature
Nice to have
• Door plate, Flyersheet (basic structure), Envelop...

```html
<!DOCTYPE html>
<html lang="en">
<head>
<meta charset="utf-8">
<title>Verlan Consulting – Stationery</title>
<link href="https://fonts.googleapis.com/css2?family=Play:wght@400;700&display=swap" rel="stylesheet">
<style>
  :root {
    --burgundy: #8e1d1f;
    --gold: #d2b100;
    --gold-light: #e6d24c;
    --dark-grey: #4a4a4a;
    --label-grey: #7a7a7a;
    --paper: #ffffff;
    --ink: #1e1e1e;
  }
  * { box-sizing: border-box; margin: 0; padding: 0; }
  html, body { width: 1200px; height: 960px; overflow: hidden; background: #fff; }
  body { position: relative; font-family: "Play", Arial, sans-serif; color: var(--ink); }

  .section-label { position: absolute; font-size: 15px; color: var(--label-grey); line-height: 1.15; }

  .wordmark { position: absolute; z-index: 2; display: flex; align-items: center; gap: 0.4em;
    color: var(--burgundy); font-weight: 700; white-space: nowrap; line-height: 1; }
  .wordmark .mark-square { width: 1.3em; height: 1.3em; background: var(--burgundy); flex: none; }
  .wordmark .wordmark-text { display: flex; flex-direction: column; }

  .contact { position: absolute; z-index: 2; font-size: 11px; line-height: 1.3; }

  /* Email signature */
  .email-signature {
    position: absolute; left: 17px; top: 38px; width: 475px; height: 100px;
    background: linear-gradient(180deg, #d8d8d8 0%, #f2f2f2 45%, #cfcfcf 100%);
    box-shadow: 0 2px 8px rgba(0,0,0,.25); overflow: hidden;
  }
  .email-signature .decor { position: absolute; left: 0; top: 0; width: 230px; height: 82px;
    background: linear-gradient(120deg, rgba(142,29,31,.35), rgba(160,160,160,.25) 60%, transparent); }
  .email-signature .wordmark { left: 14px; top: 31px; font-size: 18px; }
  .email-signature .contact { left: 362px; top: 32px; font-size: 8px; line-height: 1.25; }
  .email-signature .band { position: absolute; left: 0; right: 0; bottom: 0; height: 18px;
    background: linear-gradient(90deg, #9a9a9a 0 30%, var(--gold) 30% 80%, var(--burgundy) 80%); }
  .email-signature .band span { position: absolute; left: 245px; top: 3px; font-size: 9px; }

  /* Envelope */
  .envelope {
    position: absolute; left: 17px; top: 174px; width: 695px; height: 300px;
    background: var(--paper); box-shadow: 0 2px 10px rgba(0,0,0,.25); overflow: hidden;
  }
  .top-bar { position: absolute; left: 0; right: 0; top: 0; height: 18px; background: var(--dark-grey); }
  .envelope .decor { position: absolute; right: 0; top: 18px; width: 380px; height: 260px;
    background: linear-gradient(135deg, rgba(142,29,31,.12), rgba(142,29,31,.04) 70%, transparent); }
  .envelope .wordmark { left: 24px; top: 30px; font-size: 20px; }
  .envelope .contact { left: 24px; top: 206px; }
  .bottom-band { position: absolute; left: 0; right: 0; bottom: 0; height: 22px;
    background: linear-gradient(90deg, var(--burgundy) 0 22%, var(--gold) 22% 45%, var(--gold-light) 60%, rgba(255,255,255,0)); }
  .bottom-band span { position: absolute; top: 3px; font-size: 14px; color: #222; }
  .envelope .bottom-band span { left: 186px; }

  /* Letterhead */
  .letterhead {
    position: absolute; left: 506px; top: 61px; width: 682px; height: 881px;
    background: var(--paper); box-shadow: 0 2px 10px rgba(0,0,0,.25); overflow: hidden;
  }
  .letterhead .top-bar { background: linear-gradient(90deg, #555 0 50%, #ddd 60%, #e4e4e4); }
  .letterhead .decor { position: absolute; right: 0; top: 100px; width: 340px; height: 750px;
    background: linear-gradient(160deg, rgba(142,29,31,.12), rgba(142,29,31,.05) 60%, rgba(142,29,31,.02)); }
  .letterhead .wordmark { left: 32px; top: 33px; font-size: 24px; }
  .letterhead .contact { left: 30px; top: 778px; font-size: 12px; }
  .letterhead .bottom-band { height: 17px;
    background: linear-gradient(90deg, var(--burgundy) 0 25%, var(--gold) 25% 60%, var(--gold-light) 75%, rgba(255,255,255,0)); }
  .letterhead .bottom-band span { left: 212px; top: 1px; font-size: 12px; }

  /* Business card front */
  .card-front {
    position: absolute; left: 18px; top: 504px; width: 346px; height: 212px;
    background: linear-gradient(180deg, #d9d9d9 0%, #8a8a8a 35%, #2f2f2f 70%, #1c1c1c 100%);
    box-shadow: 0 2px 8px rgba(0,0,0,.3); overflow: hidden;
  }
  .card-front .decor { position: absolute; right: 0; top: 0; width: 170px; height: 212px;
    background: linear-gradient(135deg, rgba(142,29,31,.45), rgba(120,30,32,.85) 60%, rgba(60,20,20,.8)); }
  .card-front .wordmark { left: 40px; top: 16px; font-size: 20px; }
  .card-front .name-bar { position: absolute; z-index: 2; left: 0; top: 88px; width: 280px; height: 40px;
    background: linear-gradient(90deg, var(--burgundy) 0 8%, var(--gold) 8% 55%, rgba(210,177,0,0)); }
  .card-front .name { position: absolute; left: 36px; top: 5px; font-size: 13px; color: #fff; }
  .card-front .role { position: absolute; left: 36px; top: 22px; font-size: 7px; color: #fff; }
  .card-front .contact { left: 37px; top: 140px; font-size: 10.5px; color: #fff; line-height: 1.27; }

  /* Business card back */
  .card-back {
    position: absolute; left: 145px; top: 731px; width: 347px; height: 212px;
    background: radial-gradient(ellipse at 65% 45%, #f4f4f4 0%, #c4c4c4 55%, #7c7c7c 100%);
    box-shadow: 0 2px 8px rgba(0,0,0,.3); overflow: hidden;
  }
  .card-back .decor { position: absolute; left: 0; top: 0; width: 150px; height: 212px;
    background: linear-gradient(120deg, rgba(142,29,31,.55), rgba(120,120,120,.45) 55%, rgba(120,120,120,0)); }
  .card-back .wordmark { left: 168px; top: 82px; font-size: 21px; }
  .card-back .url { position: absolute; right: 24px; bottom: 8px; font-size: 9px; color: #555; }
</style>
</head>
<body>

  <div class="section-label" style="left:17px; top:12px;">Email Signature</div>
  <section class="email-signature">
    <div class="decor" role="img" aria-label="Soft burgundy and grey background sweep"></div>
    <div class="wordmark"><span class="mark-square"></span><span class="wordmark-text"><span>Verlan</span><span>Consulting</span></span></div>
    <div class="contact">Adress: 18, Rue des Lilas L-2340<br>Luxembourg<br>Phone: +352 4815 302<br>Fax: +352 4815 309</div>
    <div class="band"><span>www.verlanconsulting.com</span></div>
  </section>

  <div class="section-label" style="left:506px; top:36px;">Business Papers</div>
  <section class="letterhead">
    <div class="top-bar"></div>
    <div class="decor" role="img" aria-label="Faint burgundy background sweep"></div>
    <div class="wordmark"><span class="mark-square"></span><span class="wordmark-text"><span>Verlan</span><span>Consulting</span></span></div>
    <div class="contact">Adress: 18, Rue des Lilas L-2340<br>Luxembourg<br>Phone: +352 4815 302<br>Fax: +352 4815 309<br>Email: office@verlanconsulting.lu</div>
    <div class="bottom-band"><span>www.verlanconsulting.com</span></div>
  </section>

  <section class="envelope">
    <div class="top-bar"></div>
    <div class="decor" role="img" aria-label="Faint burgundy background sweep"></div>
    <div class="wordmark"><span class="mark-square"></span><span class="wordmark-text"><span>Verlan</span><span>Consulting</span></span></div>
    <div class="contact">Adress: 18, Rue des Lilas L-2340<br>Luxembourg<br>Phone: +352 4815 302<br>Fax: +352 4815 309<br>Email: office@verlanconsulting.lu</div>
    <div class="bottom-band"><span>www.verlanconsulting.com</span></div>
  </section>

  <div class="section-label" style="left:19px; top:486px;">Business Cards: Front</div>
  <section class="card-front">
    <div class="decor" role="img" aria-label="Burgundy and dark grey background sweep"></div>
    <div class="wordmark"><span class="mark-square"></span><span class="wordmark-text"><span>Verlan</span><span>Consulting</span></span></div>
    <div class="name-bar">
      <div class="name">Martin Keller</div>
      <div class="role">CEO</div>
    </div>
    <div class="contact">Adress: 18, Rue des Lilas L-2340<br>Luxembourg<br>Phone: +352 4815 302<br>Fax: +352 4815 309<br>www.verlanconsulting.com</div>
  </section>

  <div class="section-label" style="left:18px; top:732px;">Business Cards:<br>Back</div>
  <section class="card-back">
    <div class="decor" role="img" aria-label="Burgundy and grey background sweep"></div>
    <div class="wordmark"><span class="mark-square"></span><span class="wordmark-text"><span>Verlan</span><span>Consulting</span></span></div>
    <div class="url">www.verlanconsulting.com</div>
  </section>

</body>
</html>
```